Shopify Design for a Homeopathic Shop

The design should let the user give a feeling of luxury and naturality(earthy).

We want to build up a alternative medicine luxury brand. The user should have a feeling of trust when visiting our shop. We stand for natural remedies.

Target Market(s)

Alternative / Left

Industry/Entity Type

Alternative Medicine

Font styles to use
Sans Serif

Colors

Designer to choose colors to be used in the design.

```html
<!DOCTYPE html>
<html lang="en">
<head>
<meta charset="utf-8">
<title>Verdalis – Homeopathic Remedies</title>
<link href="https://fonts.googleapis.com/css2?family=Lato:wght@400;700&family=Fira+Sans:wght@600&display=swap" rel="stylesheet">
<style>
:root{
  --green:#7dc242;
  --green-dark:#1f7a34;
  --price:#d7262b;
  --text:#333;
  --muted:#555;
  --line:#dcdcdc;
  --gray-band:#f3f3f3;
  --footer:#1c1c1c;
  --white:#fff;
}
*{margin:0;padding:0;box-sizing:border-box}
html,body{width:1200px;height:3429px;overflow:hidden}
body{font-family:'Lato',sans-serif;color:var(--text);background:var(--white);position:relative}
a{color:inherit;text-decoration:none}

/* header */
.site-header{position:absolute;left:0;top:0;width:1200px;height:94px;border-bottom:1px solid #eee}
.brand{position:absolute;left:80px;top:30px;display:flex;align-items:center;gap:8px;font-size:28px;color:var(--green);font-weight:400;letter-spacing:1px}
.brand .dot{width:12px;height:12px;border-radius:50%;background:var(--green-dark)}
.main-nav{position:absolute;top:45px;left:0;font-size:14.5px;color:#444}
.main-nav a{position:absolute;white-space:nowrap;color:#444}
.cart{position:absolute;left:964px;top:38px;display:flex;align-items:flex-end;gap:4px;font-size:15px;color:#444}
.cart-badge{position:absolute;left:970px;top:21px;width:20px;height:20px;border-radius:50%;background:var(--green-dark);color:#fff;font-size:11px;text-align:center;line-height:20px}
.header-icon{position:absolute;top:41px}

/* hero */
.hero{position:absolute;left:0;top:94px;width:1200px;height:503px;
  background:
    radial-gradient(ellipse 170px 120px at 930px 330px,rgba(240,240,235,.95),rgba(240,240,235,0) 75%),
    radial-gradient(ellipse 140px 180px at 770px 260px,rgba(150,70,20,.95),rgba(150,70,20,0) 75%),
    radial-gradient(ellipse 110px 160px at 580px 240px,rgba(120,140,110,.55),rgba(120,140,110,0) 75%),
    radial-gradient(ellipse 420px 200px at 650px 430px,rgba(110,85,60,.9),rgba(110,85,60,0) 80%),
    radial-gradient(ellipse 260px 240px at 1120px 360px,rgba(95,135,40,.9),rgba(95,135,40,0) 80%),
    radial-gradient(ellipse 300px 260px at 120px 430px,rgba(40,80,35,.95),rgba(40,80,35,0) 80%),
    linear-gradient(180deg,#45672e 0%,#5a7a3a 35%,#5d513c 70%,#3f4f2a 100%)}
.hero::after{content:"";position:absolute;inset:0;background:linear-gradient(90deg,rgba(20,35,15,.45) 0%,rgba(20,35,15,.15) 40%,rgba(0,0,0,0) 60%)}
.hero-copy{position:absolute;left:80px;top:170px;color:#fff;z-index:1}
.hero-copy h1{font-weight:400;font-size:32px;line-height:39px;letter-spacing:-.3px}
.hero-copy p{font-size:13px;line-height:17px;margin-top:12px;width:320px}
.btn{display:block;background:var(--green);color:#fff;font-weight:700;font-size:13px;text-align:center}
.hero .btn{position:absolute;left:80px;top:305px;width:173px;height:44px;line-height:44px;z-index:1}

/* features */
.feature{position:absolute;top:641px;width:327px;height:149px;border:1px solid var(--line);display:flex;align-items:center;padding-left:28px;gap:16px}
.feature h3{font-size:13px;font-weight:700;color:#333}
.feature p{font-size:13px;color:#555;margin-top:5px}

.section-title{position:absolute;left:0;width:1200px;text-align:center;font-weight:400;font-size:36px;letter-spacing:1.5px;color:#333}

/* product cards */
.product{position:absolute;width:237px;text-align:center}
.product .thumb{height:249px;border:1px solid var(--line);display:flex;align-items:center;justify-content:center;background:#fff}
.product .shot{width:190px;height:220px}
.product .name{margin-top:20px;font-size:14px;letter-spacing:1.5px;color:#444}
.product .price{margin-top:6px;font-size:19px;letter-spacing:1.5px;color:var(--price)}
.btn-more{position:absolute;width:173px;height:46px;line-height:46px}

/* promo band */
.promo{position:absolute;left:0;top:1360px;width:1200px;height:488px;background:var(--gray-band)}
.promo h2{position:absolute;left:80px;top:156px;font-family:'Fira Sans',sans-serif;font-weight:600;font-size:32px;line-height:38px;color:var(--green-dark)}
.promo h2 span{color:var(--green)}
.promo p{position:absolute;left:80px;top:243px;width:320px;font-size:13px;line-height:17px;color:#444}
.promo .btn{position:absolute;left:80px;top:292px;width:173px;height:46px;line-height:46px}
.promo-visual{position:absolute;left:446px;top:24px;width:700px;height:440px;
  background:
    radial-gradient(ellipse 60px 40px at 320px 230px,rgba(255,255,255,.95),rgba(255,255,255,0) 80%),
    radial-gradient(ellipse 150px 60px at 280px 380px,rgba(255,255,255,.95),rgba(255,255,255,0) 80%),
    radial-gradient(ellipse 150px 110px at 600px 330px,rgba(80,160,45,.9),rgba(80,160,45,0) 80%),
    radial-gradient(ellipse 110px 100px at 110px 250px,rgba(220,180,40,.85),rgba(220,180,40,0) 80%),
    radial-gradient(ellipse 70px 170px at 500px 220px,rgba(140,70,15,.95),rgba(140,70,15,0) 80%),
    radial-gradient(ellipse 60px 140px at 390px 240px,rgba(170,95,30,.9),rgba(170,95,30,0) 80%),
    radial-gradient(ellipse 30px 60px at 500px 40px,rgba(255,255,255,.9),rgba(255,255,255,0) 80%)}

/* blog */
.post{position:absolute;top:2420px;width:336px;height:389px;border:1px solid var(--line)}
.post .image{position:absolute;left:12px;top:12px;width:312px;height:208px}
.post .meta{position:absolute;left:16px;top:230px;right:16px;display:flex;font-size:13px;color:#555;align-items:center;gap:5px}
.post .meta .stats{margin-left:auto;display:flex;gap:14px;align-items:center}
.post .meta .stats span{display:flex;gap:4px;align-items:center}
.post .meta-rule{position:absolute;left:12px;right:12px;top:252px;border-top:1px solid var(--line)}
.post h3{position:absolute;left:18px;top:264px;font-size:15px;font-weight:400;color:#444}
.post p{position:absolute;left:18px;top:288px;right:14px;font-size:13.5px;line-height:16px;color:#555}
.post .continue{position:absolute;left:18px;top:352px;font-size:12.5px;color:#555;display:flex;gap:8px;align-items:center}

/* newsletter */
.newsletter-title{position:absolute;left:0;top:2920px;width:1200px;text-align:center;font-size:32px;letter-spacing:1.5px;font-weight:400}
.newsletter-sub{position:absolute;left:0;top:2966px;width:1200px;text-align:center;font-size:13px;color:#555}
.email{position:absolute;left:329px;top:3001px;width:431px;height:46px;border:1px solid #ccc;font-size:13px;font-style:italic;color:#888;padding-left:14px;line-height:44px}
.submit{position:absolute;left:778px;top:3001px;width:173px;height:46px;line-height:46px}

/* footer */
.site-footer{position:absolute;left:0;top:3117px;width:1200px;height:312px;background:var(--footer);color:#e6e6e6}
.site-footer .brand{left:80px;top:50px;color:#fff}
.site-footer .brand .dot{background:#fff}
.foot-col h4{position:absolute;top:52px;font-weight:400;font-size:17px;letter-spacing:1px;color:#fff}
.foot-col ul{position:absolute;top:98px;list-style:none;font-size:13.5px}
.foot-col li{height:25.5px;display:flex;align-items:center;gap:14px}
.foot-col li::before{content:">";font-size:11px}
.social li::before{content:none}
.social .ico{width:17px;height:17px;border-radius:50%;background:var(--green)}
.footer-rule{position:absolute;left:0;top:256px;width:1200px;border-top:1px solid #555}
.copyright{position:absolute;left:80px;top:276px;font-size:14px;letter-spacing:.5px}
.payments{position:absolute;left:853px;top:266px;display:flex;gap:6px}
.payments span{width:49px;height:30px;background:#fff;color:#222;font-size:9px;font-weight:700;display:flex;align-items:center;justify-content:center;border-radius:2px}
</style>
</head>
<body>

<header class="site-header">
  <div class="brand"><span class="dot"></span>Verdalis</div>
  <nav class="main-nav">
    <a style="left:410px">Home</a>
    <a style="left:490px">About us</a>
    <a style="left:589px">Shop</a>
    <a style="left:664px">Blogs</a>
    <a style="left:741px">Contact us</a>
  </nav>
  <span class="cart-badge">1</span>
  <div class="cart">
    <svg width="26" height="24" viewBox="0 0 26 24" fill="none" stroke="#444" stroke-width="1.6"><path d="M1 2h4l3 13h13l3-9H7"/><circle cx="10" cy="20" r="2"/><circle cx="19" cy="20" r="2"/></svg>
    Cart
  </div>
  <svg class="header-icon" style="left:1054px" width="22" height="22" viewBox="0 0 22 22" fill="none" stroke="#333" stroke-width="2"><circle cx="9" cy="9" r="7"/><path d="M14 14l7 7"/></svg>
  <svg class="header-icon" style="left:1101px" width="20" height="18" viewBox="0 0 20 18" fill="#333"><rect y="1" width="20" height="3"/><rect y="7.5" width="20" height="3"/><rect y="14" width="20" height="3"/></svg>
</header>

<section class="hero" role="img" aria-label="Amber remedy bottles, glass jar, white mortar and pestle and fresh green herbs on a rustic wooden table">
  <div class="hero-copy">
    <h1>We Help You to live a<br>Healthy Life</h1>
    <p>Lorem Ipsum is simply dummy text of the printing and typesetting industry.</p>
  </div>
  <a class="btn">Shop Now &gt;&gt;</a>
</section>

<div class="feature" style="left:80px">
  <svg width="58" height="34" viewBox="0 0 58 34" fill="var(--green-dark)"><rect x="14" y="4" width="26" height="20"/><path d="M40 10h9l7 8v6H40z"/><circle cx="22" cy="27" r="5"/><circle cx="48" cy="27" r="5"/><rect x="0" y="8" width="11" height="2"/><rect x="3" y="14" width="8" height="2"/><rect x="6" y="20" width="5" height="2"/></svg>
  <div><h3>Free Shipping Worldwide</h3><p>Lorem ipsum is simply dummy</p></div>
</div>
<div class="feature" style="left:435px;padding-left:48px">
  <svg width="40" height="42" viewBox="0 0 40 42" fill="var(--green-dark)"><circle cx="20" cy="12" r="10"/><path d="M2 42c0-11 8-17 18-17s18 6 18 17z"/></svg>
  <div><h3>24/7 Dedicated Support</h3><p>Lorem ipsum is simply dummy</p></div>
</div>
<div class="feature" style="left:792px;padding-left:48px">
  <svg width="34" height="46" viewBox="0 0 34 46" fill="var(--green-dark)"><path d="M8 26l-6 18 7-4 4 6 5-16zM26 26l6 18-7-4-4 6-5-16z"/><circle cx="17" cy="16" r="15"/><path d="M17 7l3 6 6 1-4 4 1 6-6-3-6 3 1-6-4-4 6-1z" fill="#fff"/></svg>
  <div><h3>Money Back Guarantee</h3><p>Lorem ipsum is simply dummy</p></div>
</div>

<h2 class="section-title" style="top:828px">Featured Products</h2>

<div class="product" style="left:80px;top:913px"><div class="thumb"><div class="shot" role="img" aria-label="Homeopathic tablet bottle beside its white and green box" style="background:radial-gradient(ellipse 40px 70px at 60px 130px,rgba(90,40,20,.85),rgba(90,40,20,0) 80%),radial-gradient(ellipse 55px 90px at 130px 105px,rgba(225,235,225,1),rgba(225,235,225,0) 85%),radial-gradient(ellipse 20px 20px at 120px 110px,rgba(235,100,30,.9),rgba(235,100,30,0) 85%)"></div></div><div class="name">Product Name</div><div class="price">$00.00</div></div>
<div class="product" style="left:347px;top:913px"><div class="thumb"><div class="shot" role="img" aria-label="Mother tincture bottle with red dropper cap" style="background:radial-gradient(ellipse 25px 40px at 95px 45px,rgba(220,40,45,1),rgba(220,40,45,0) 85%),radial-gradient(ellipse 42px 75px at 95px 140px,rgba(40,25,20,1),rgba(40,25,20,0) 85%)"></div></div><div class="name">Product Name</div><div class="price">$00.00</div></div>
<div class="product" style="left:616px;top:913px"><div class="thumb"><div class="shot" role="img" aria-label="Amber remedy bottle with white cap and label" style="background:radial-gradient(ellipse 40px 30px at 95px 45px,rgba(235,235,235,1),rgba(235,235,235,0) 85%),radial-gradient(ellipse 50px 75px at 95px 140px,rgba(130,40,15,1),rgba(130,40,15,0) 85%)"></div></div><div class="name">Product Name</div><div class="price">$00.00</div></div>
<div class="product" style="left:883px;top:913px"><div class="thumb"><div class="shot" role="img" aria-label="Children's syrup bottle beside a bright yellow box" style="background:radial-gradient(ellipse 40px 80px at 60px 130px,rgba(110,40,15,.95),rgba(110,40,15,0) 85%),radial-gradient(ellipse 50px 100px at 135px 110px,rgba(240,210,60,1),rgba(240,210,60,0) 85%),radial-gradient(ellipse 20px 20px at 140px 120px,rgba(215,40,40,.8),rgba(215,40,40,0) 85%)"></div></div><div class="name">Product Name</div><div class="price">$00.00</div></div>

<a class="btn btn-more" style="left:515px;top:1271px">View More</a>

<section class="promo">
  <h2>Homeopathy Cures<br><span>No Side Effects</span></h2>
  <p>Lorem Ipsum is simply dummy text of the printing and typesetting industry.</p>
  <a class="btn">Shop Now &gt;&gt;</a>
  <div class="promo-visual" role="img" aria-label="Amber remedy bottles with daisies, yellow wild flowers, mint leaves and white pills"></div>
</section>

<h2 class="section-title" style="top:1902px">Best Seller</h2>

<div class="product" style="left:80px;top:1986px"><div class="thumb"><div class="shot" role="img" aria-label="Two amber essential oil bottles with navy caps" style="background:radial-gradient(ellipse 22px 30px at 75px 40px,rgba(45,55,85,1),rgba(45,55,85,0) 85%),radial-gradient(ellipse 42px 75px at 75px 140px,rgba(200,140,45,1),rgba(200,140,45,0) 85%),radial-gradient(ellipse 25px 50px at 135px 160px,rgba(190,130,40,.9),rgba(190,130,40,0) 85%)"></div></div><div class="name">Product Name</div><div class="price">$00.00</div></div>
<div class="product" style="left:347px;top:1986px"><div class="thumb"><div class="shot" role="img" aria-label="Children's remedy oil bottle with orange label" style="background:radial-gradient(ellipse 28px 30px at 95px 40px,rgba(235,235,235,1),rgba(235,235,235,0) 85%),radial-gradient(ellipse 38px 75px at 95px 140px,rgba(230,110,35,1),rgba(230,110,35,0) 85%)"></div></div><div class="name">Product Name</div><div class="price">$00.00</div></div>
<div class="product" style="left:616px;top:1986px"><div class="thumb"><div class="shot" role="img" aria-label="Drops bottle beside a white and peach box" style="background:radial-gradient(ellipse 50px 100px at 70px 110px,rgba(240,230,225,1),rgba(240,230,225,0) 85%),radial-gradient(ellipse 35px 70px at 140px 140px,rgba(200,120,40,1),rgba(200,120,40,0) 85%)"></div></div><div class="name">Product Name</div><div class="price">$00.00</div></div>
<div class="product" style="left:883px;top:1986px"><div class="thumb"><div class="shot" role="img" aria-label="Remedy bottle beside a red and white box" style="background:radial-gradient(ellipse 50px 100px at 65px 110px,rgba(235,215,210,1),rgba(235,215,210,0) 85%),radial-gradient(ellipse 30px 30px at 65px 80px,rgba(190,30,40,.85),rgba(190,30,40,0) 85%),radial-gradient(ellipse 35px 65px at 140px 140px,rgba(40,25,25,1),rgba(40,25,25,0) 85%)"></div></div><div class="name">Product Name</div><div class="price">$00.00</div></div>

<h2 class="section-title" style="top:2353px">Blogs</h2>

<article class="post" style="left:69px">
  <div class="image" role="img" aria-label="Shopping cart with medicine bottles in front of a laptop" style="background:radial-gradient(ellipse 110px 60px at 160px 110px,rgba(200,60,50,.55),rgba(200,60,50,0) 85%),radial-gradient(ellipse 130px 60px at 130px 40px,rgba(190,225,90,.9),rgba(190,225,90,0) 85%),linear-gradient(160deg,#e3e7c8,#e8e4de 50%,#a9a6a2)"></div>
  <div class="meta"><svg width="11" height="11" viewBox="0 0 11 11" fill="none" stroke="#555"><rect x=".5" y="1.5" width="10" height="9"/><path d="M.5 4h10"/></svg>June 24, 2019<div class="stats"><span><svg width="13" height="12" viewBox="0 0 13 12" fill="none" stroke="#555"><path d="M6.5 1C3 1 1 3 1 5.3c0 1.2.6 2.2 1.6 3L2 11l3-1.6c.5.1 1 .2 1.5.2C10 9.6 12 7.6 12 5.3S10 1 6.5 1z"/></svg>20</span><span><svg width="13" height="12" viewBox="0 0 13 12" fill="none" stroke="#555"><path d="M6.5 11S1 7.5 1 4a2.8 2.8 0 015.5-1A2.8 2.8 0 0112 4c0 3.5-5.5 7-5.5 7z"/></svg>12</span></div></div>
  <div class="meta-rule"></div>
  <h3>What is Lorem Ipsum?</h3>
  <p>Lorem Ipsum is simply dummy&nbsp; the printing and typesetting industry. Lorem Ipsum has been the in the standard dummy.</p>
  <div class="continue">Continue.. <svg width="14" height="14" viewBox="0 0 14 14" fill="none" stroke="#444"><circle cx="7" cy="7" r="6"/><path d="M6 4.5L8.5 7 6 9.5"/></svg></div>
</article>
<article class="post" style="left:431px">
  <div class="image" role="img" aria-label="Hand holding a small dropper vial over green plants" style="background:radial-gradient(ellipse 90px 50px at 220px 80px,rgba(235,235,235,.75),rgba(235,235,235,0) 85%),radial-gradient(ellipse 20px 30px at 165px 80px,rgba(200,130,40,.9),rgba(200,130,40,0) 85%),radial-gradient(ellipse 120px 80px at 90px 140px,rgba(70,120,60,.8),rgba(70,120,60,0) 85%),linear-gradient(135deg,#1f2f27,#2f4638 50%,#1a2520)"></div>
  <div class="meta"><svg width="11" height="11" viewBox="0 0 11 11" fill="none" stroke="#555"><rect x=".5" y="1.5" width="10" height="9"/><path d="M.5 4h10"/></svg>June 22, 2019<div class="stats"><span><svg width="13" height="12" viewBox="0 0 13 12" fill="none" stroke="#555"><path d="M6.5 1C3 1 1 3 1 5.3c0 1.2.6 2.2 1.6 3L2 11l3-1.6c.5.1 1 .2 1.5.2C10 9.6 12 7.6 12 5.3S10 1 6.5 1z"/></svg>20</span><span><svg width="13" height="12" viewBox="0 0 13 12" fill="none" stroke="#555"><path d="M6.5 11S1 7.5 1 4a2.8 2.8 0 015.5-1A2.8 2.8 0 0112 4c0 3.5-5.5 7-5.5 7z"/></svg>12</span></div></div>
  <div class="meta-rule"></div>
  <h3>What is Lorem Ipsum?</h3>
  <p>Lorem Ipsum is simply dummy&nbsp; the printing and typesetting industry. Lorem Ipsum has been the in the standard dummy.</p>
  <div class="continue">Continue.. <svg width="14" height="14" viewBox="0 0 14 14" fill="none" stroke="#444"><circle cx="7" cy="7" r="6"/><path d="M6 4.5L8.5 7 6 9.5"/></svg></div>
</article>
<article class="post" style="left:793px">
  <div class="image" role="img" aria-label="Small glass vials of white pills on a wooden table with leaves" style="background:radial-gradient(ellipse 110px 60px at 200px 130px,rgba(235,235,230,.8),rgba(235,235,230,0) 85%),radial-gradient(ellipse 120px 70px at 60px 40px,rgba(235,200,80,.9),rgba(235,200,80,0) 85%),linear-gradient(170deg,#b79a45,#6f7a3a 45%,#4a3624 80%,#2f2218)"></div>
  <div class="meta"><svg width="11" height="11" viewBox="0 0 11 11" fill="none" stroke="#555"><rect x=".5" y="1.5" width="10" height="9"/><path d="M.5 4h10"/></svg>June 20, 2019<div class="stats"><span><svg width="13" height="12" viewBox="0 0 13 12" fill="none" stroke="#555"><path d="M6.5 1C3 1 1 3 1 5.3c0 1.2.6 2.2 1.6 3L2 11l3-1.6c.5.1 1 .2 1.5.2C10 9.6 12 7.6 12 5.3S10 1 6.5 1z"/></svg>20</span><span><svg width="13" height="12" viewBox="0 0 13 12" fill="none" stroke="#555"><path d="M6.5 11S1 7.5 1 4a2.8 2.8 0 015.5-1A2.8 2.8 0 0112 4c0 3.5-5.5 7-5.5 7z"/></svg>12</span></div></div>
  <div class="meta-rule"></div>
  <h3>What is Lorem Ipsum?</h3>
  <p>Lorem Ipsum is simply dummy&nbsp; the printing and typesetting industry. Lorem Ipsum has been the in the standard dummy.</p>
  <div class="continue">Continue.. <svg width="14" height="14" viewBox="0 0 14 14" fill="none" stroke="#444"><circle cx="7" cy="7" r="6"/><path d="M6 4.5L8.5 7 6 9.5"/></svg></div>
</article>

<a class="btn btn-more" style="left:516px;top:2838px">View More</a>

<h2 class="newsletter-title">Join Our Newletter</h2>
<p class="newsletter-sub">Lorem Ipsum is simply dummy.</p>
<div class="email">Email Here</div>
<a class="btn submit">Submit</a>

<footer class="site-footer">
  <div class="brand"><span class="dot"></span>Verdalis</div>
  <div class="foot-col">
    <ul style="left:80px"><li>Home</li><li>About us</li><li>Shop</li><li>Blogs</li><li>Contact us</li></ul>
  </div>
  <div class="foot-col">
    <h4 style="left:355px">Why Buy From us</h4>
    <ul style="left:355px"><li>Shipping &amp; Returns</li><li>Secure Shopping</li><li>International Shopping</li><li>Group Sales</li><li>Affiliates</li></ul>
  </div>
  <div class="foot-col">
    <h4 style="left:665px">My Account</h4>
    <ul style="left:668px"><li>Sign In</li><li>View Cart</li><li>My Product</li><li>Track My Order</li><li>Help</li></ul>
  </div>
  <div class="foot-col social">
    <h4 style="left:939px;top:54px">Follow us</h4>
    <ul style="left:939px;top:100px"><li><span class="ico"></span>Friendbook</li><li><span class="ico"></span>Snapgram</li><li><span class="ico"></span>Chirper</li><li><span class="ico"></span>Workline</li><li><span class="ico"></span>Viewtube</li></ul>
  </div>
  <div class="footer-rule"></div>
  <p class="copyright">Copyright©2019 Verdalis, All right reserved</p>
  <div class="payments"><span>Payra</span><span>Findcard</span><span>Cardio</span><span>Duocard</span><span>Shopzone</span></div>
</footer>

</body>
</html>
```